Kestrel Roofing & Restoration Business Card Design

Lookiing for a double sided business card design that will have rounded corners, will look good with Spot UV, Soft Laminate, or Gloss
Front of card should have Logo, Name and Contact Info, License numbers
Back of card should have Logo, maybe other small details

```html
<!DOCTYPE html>
<html lang="en">
<head>
<meta charset="utf-8">
<title>Kestrel Roofing &amp; Restoration — Business Card</title>
<link rel="stylesheet" href="https://fonts.googleapis.com/css2?family=Arimo:wght@400;700&family=Poppins:wght@600&display=swap">
<style>
  :root {
    --page: #e4e4e4;
    --card-top: #3e3e3e;
    --card-bottom: #2f2f2f;
    --accent: #1ba3e2;
    --ink: #ffffff;
    --rule: #cfcfcf;
  }
  * { box-sizing: border-box; margin: 0; padding: 0; }
  html, body { width: 1200px; height: 1200px; overflow: hidden; }
  body {
    background: var(--page);
    font-family: "Arimo", Arial, sans-serif;
    color: var(--ink);
    position: relative;
  }
  .card {
    position: absolute;
    left: 240px;
    width: 720px;
    height: 410px;
    border-radius: 18px;
    background: linear-gradient(180deg, var(--card-top), var(--card-bottom));
  }
  .card--front { top: 160px; }
  .card--back { top: 650px; }

  /* front */
  .identity {
    position: absolute;
    right: 338px;
    top: 150px;
    text-align: right;
    font-size: 17px;
    line-height: 22px;
  }
  .identity__name {
    color: var(--accent);
    font-weight: 700;
    font-size: 29px;
    line-height: 36px;
    margin-bottom: 2px;
  }
  .divider {
    position: absolute;
    left: 400px;
    top: 150px;
    width: 1px;
    height: 116px;
    background: var(--rule);
  }
  .contact {
    position: absolute;
    left: 416px;
    top: 150px;
    font-size: 17px;
    line-height: 21.5px;
    list-style: none;
  }
  .contact__license { font-size: 18px; margin-bottom: 4px; }
  .contact__item { display: flex; align-items: center; gap: 10px; }
  .contact__item svg { width: 15px; height: 15px; flex: none; }

  /* back */
  .brand {
    position: absolute;
    left: 0; right: 0; top: 0; bottom: 0;
    display: flex;
    align-items: center;
    justify-content: center;
    gap: 18px;
  }
  .brand__mark {
    width: 26px; height: 26px;
    background: var(--accent);
  }
  .brand__name {
    font-family: "Poppins", Arial, sans-serif;
    font-weight: 600;
    font-size: 36px;
    line-height: 46px;
    letter-spacing: 0.5px;
    color: var(--ink);
  }
</style>
</head>
<body>
  <section class="card card--front" aria-label="Card front">
    <div class="identity">
      <p class="identity__name">DANIEL HARLOW</p>
      <p>President</p>
      <p>412 Ridgeline Road</p>
      <p>Whitehorse, Canada 58210</p>
    </div>
    <div class="divider"></div>
    <ul class="contact">
      <li class="contact__license">LIC.NO 5120</li>
      <li class="contact__item">
        <svg viewBox="0 0 16 16" fill="var(--accent)"><path d="M3.2 1.2l2.4-.4 1.6 3.6-1.7 1.2a9 9 0 0 0 4.9 4.9l1.2-1.7 3.6 1.6-.4 2.4c-.2.9-1 1.4-1.9 1.3C6.8 13.5 2.5 9.2 1.9 3.1c-.1-.9.4-1.7 1.3-1.9z"/></svg>
        555-214-8830
      </li>
      <li class="contact__item">
        <svg viewBox="0 0 16 16" fill="none" stroke="var(--accent)" stroke-width="1.8"><rect x="4" y="1" width="8" height="14" rx="1.2"/><line x1="7" y1="12.5" x2="9" y2="12.5"/></svg>
        555-390-1746
      </li>
      <li class="contact__item">
        <svg viewBox="0 0 16 16" fill="var(--accent)"><path d="M1 3h14v10H1z"/><path d="M1.5 3.5L8 9l6.5-5.5" fill="none" stroke="#333" stroke-width="1.4"/></svg>
        info@kestrelroofing.com
      </li>
      <li class="contact__item">
        <svg viewBox="0 0 16 16"><circle cx="8" cy="8" r="7" fill="var(--accent)"/><path d="M5 4c2 1 1 3 3 3s1 3-1 4M10 3c-1 2 1 3 3 3" fill="none" stroke="#333" stroke-width="1.2"/></svg>
        www.kestrelroofing.com
      </li>
    </ul>
  </section>

  <section class="card card--back" aria-label="Card back">
    <div class="brand">
      <span class="brand__mark"></span>
      <p class="brand__name">KESTREL ROOFING &amp;<br>RESTORATION</p>
    </div>
  </section>
</body>
</html>
```